Vantro #27 - MEN'S NATURAL THERAPEUTIC INTIMATE WASH

Men's Natural Therapeutic INTIMATE Wash
VANTRO #27

Design a 4 oz. stand up tube with flip top cap...
To be packaged in a carton/box

Formula contains Tea Tree OIL
Aloe Vera Gel
Coconut Oil

PRODUCT IS A WASH/SOAP

Helps with
- Jock Itch (tinea cruris)
- Skin Rashes
- Candida
- Itchy Skin

COLORS ON TUBE: Gray, Black, Lime Electric Green and Blue

PRODUCT FOR MEN!

Target Market(s)

MEN

Industry/Entity Type

Retail

Font styles to use
Sans Serif

Colors
9bcb3b
abd036
33a6d7
000000
c9c9c9

Requirements
Must have
• Colors... black, gray, electric green and blue
Nice to have
• Needs to look masculine appeal to the male consumer

```html
<!DOCTYPE html>
<html lang="en">
<head>
<meta charset="utf-8">
<title>Vantro #27 – Men's Natural Therapeutic Intimate Wash – Carton &amp; Tube</title>
<link rel="stylesheet" href="https://fonts.googleapis.com/css2?family=Oswald:wght@600;700&family=Arimo:wght@400;700&display=swap">
<style>
  :root{
    --lime:#9bcb3b;
    --lime-bright:#abd036;
    --blue:#33a6d7;
    --black:#000000;
    --panel-black:#231f20;
    --gray:#c9c9c9;
    --gray-dark:#8a8c8e;
    --white:#ffffff;
    --line:#111111;
  }
  *{margin:0;padding:0;box-sizing:border-box}
  html,body{width:1200px;height:1067px;overflow:hidden;background:var(--white)}
  .canvas{position:relative;width:1200px;height:1067px;font-family:"Arimo",Arial,sans-serif}
  .dieline{position:absolute;left:0;top:0}
  .abs{position:absolute}
  .brand{display:flex;align-items:center;justify-content:center;gap:6px;
    font-family:"Oswald","Arial Narrow",sans-serif;font-weight:700;color:var(--black);white-space:nowrap;line-height:1}
  .brand .dot{border-radius:50%;background:var(--blue);flex:none}
  .brand.on-dark{color:var(--white)}
  .headline{font-family:"Oswald","Arial Narrow",sans-serif;font-weight:700;text-align:center;line-height:1.15;text-transform:uppercase}
  .list{text-align:center;color:var(--white);font-size:14px;line-height:20px}
  .bullets{list-style:none;font-size:14.5px;line-height:20px;color:var(--white)}
  .bullets li::before{content:"• "}
  .bullets .indent::before{content:"";padding-left:9px}
  .helps-tab{font-family:"Arimo",Arial,sans-serif;font-weight:700;font-size:14px;color:var(--white);
    border:1.5px solid var(--black);border-left:none;border-radius:0 12px 12px 0;padding:1px 12px 1px 18px;display:inline-block}
  .helps-tab.right{border-radius:12px 0 0 12px;border-left:1.5px solid var(--black);border-right:none}
  .label-band{background:var(--lime);border:1.5px solid var(--blue);text-align:center;color:var(--black)}
  .wash-box{background:var(--white);text-align:center;font-weight:700;color:var(--black)}
  .small{text-align:center;color:var(--black);font-weight:700}
</style>
</head>
<body>
<div class="canvas">

  <svg class="dieline" width="1200" height="1067" viewBox="0 0 1200 1067" xmlns="http://www.w3.org/2000/svg">
    <defs>
      <linearGradient id="tubeBody" x1="0" y1="0" x2="0" y2="1">
        <stop offset="0" stop-color="#9aaab3"/>
        <stop offset="0.12" stop-color="#c9c9c9"/>
        <stop offset="0.2" stop-color="#4a6a7a"/>
        <stop offset="0.24" stop-color="#c9c9c9"/>
        <stop offset="0.62" stop-color="#e9e9e9"/>
        <stop offset="1" stop-color="#4c4c4c"/>
      </linearGradient>
      <linearGradient id="wingLeft" x1="0" y1="0" x2="1" y2="0">
        <stop offset="0" stop-color="#9bcb3b"/>
        <stop offset="0.45" stop-color="#e6f2c8"/>
        <stop offset="1" stop-color="#5a6e33"/>
      </linearGradient>
      <linearGradient id="wingRight" x1="1" y1="0" x2="0" y2="0">
        <stop offset="0" stop-color="#9bcb3b"/>
        <stop offset="0.45" stop-color="#e6f2c8"/>
        <stop offset="1" stop-color="#5a6e33"/>
      </linearGradient>
      <linearGradient id="blackFade" x1="0" y1="0" x2="0" y2="1">
        <stop offset="0.55" stop-color="#231f20"/>
        <stop offset="1" stop-color="#3a3a3a"/>
      </linearGradient>
      <linearGradient id="limeFade" x1="0" y1="0" x2="0" y2="1">
        <stop offset="0.6" stop-color="#9bcb3b"/>
        <stop offset="1" stop-color="#8cbc30"/>
      </linearGradient>
      <linearGradient id="bottomFlap" x1="0" y1="0" x2="0" y2="1">
        <stop offset="0" stop-color="#c9c9c9"/>
        <stop offset="1" stop-color="#b8b8b8"/>
      </linearGradient>
    </defs>

    <!-- side carton: top tuck, top panel, black panel, glue flap, tab -->
    <path class="tuck-top" d="M52 100 V62 Q52 44 70 44 H258 Q276 44 276 62 V100 Z" fill="#fff" stroke="var(--line)" stroke-width="1.5"/>
    <rect x="132" y="93" width="56" height="7" fill="#fff" stroke="var(--line)" stroke-width="1.2"/>
    <rect class="panel-top" x="52" y="100" width="224" height="180" fill="var(--lime)"/>
    <path class="glue-flap" d="M14 296 L52 280 V820 L14 800 Z" fill="#fff" stroke="var(--line)" stroke-width="1.5"/>
    <rect class="panel-black" x="52" y="280" width="224" height="540" fill="url(#blackFade)"/>
    <rect x="52" y="640" width="224" height="180" fill="#2c2c2c" opacity="0.5" role="img" aria-label="Fading diamond lattice texture area"/>
    <path class="tab" d="M136 764 H192 V866 Q192 872 186 872 H142 Q136 872 136 866 Z" fill="var(--lime)" stroke="var(--line)" stroke-width="1.5"/>

    <!-- top dust flaps and centre tab -->
    <path d="M280 280 V176 H430 Q440 176 442 190 L456 280" fill="#fff" stroke="var(--line)" stroke-width="1.5"/>
    <path d="M722 280 L698 190 Q700 176 712 176 H860 V280" fill="#fff" stroke="var(--line)" stroke-width="1.5"/>
    <path d="M544 280 V234 Q544 228 550 228 H594 Q600 228 600 234 V280" fill="var(--lime)" stroke="var(--line)" stroke-width="1.5"/>

    <!-- main wrap band -->
    <rect class="band" x="276" y="280" width="590" height="540" fill="url(#limeFade)" stroke="var(--line)" stroke-width="1.5"/>

    <!-- front panel wings (decorative chevron area) -->
    <path d="M404 280 H430 Q470 560 510 820 H404 Z" fill="url(#wingLeft)" role="img" aria-label="Chevron wing pattern in lime, white and grey"/>
    <path d="M740 280 H714 Q674 560 634 820 H740 Z" fill="url(#wingRight)" role="img" aria-label="Chevron wing pattern in lime, white and grey"/>
    <!-- front tube silhouette -->
    <path d="M428 280 H716 Q670 560 638 820 H506 Q474 560 428 280 Z" fill="url(#tubeBody)"/>
    <path d="M428 280 Q474 560 506 820" fill="none" stroke="var(--blue)" stroke-width="4"/>
    <path d="M716 280 Q670 560 638 820" fill="none" stroke="var(--blue)" stroke-width="4"/>

    <!-- bottom flaps -->
    <path d="M276 820 V900 Q276 924 300 924 H452 V820" fill="#fff" stroke="var(--line)" stroke-width="1.5"/>
    <path d="M866 820 V900 Q866 924 842 924 H690 V820" fill="#fff" stroke="var(--line)" stroke-width="1.5"/>
    <path d="M458 820 V1000 H684 V820 Z" fill="url(#bottomFlap)" stroke="var(--line)" stroke-width="1.5"/>
    <path d="M458 1000 V1040 Q458 1057 476 1057 H666 Q684 1057 684 1040 V1000 Z" fill="#fff" stroke="var(--line)" stroke-width="1.5"/>
    <rect x="546" y="1000" width="56" height="7" fill="#fff" stroke="var(--line)" stroke-width="1.2"/>

    <!-- stand-up tube -->
    <rect x="990" y="296" width="208" height="20" fill="#ececec"/>
    <path d="M990 316 H1198 L1198 322 Q1180 560 1170 725 H1018 Q1008 560 990 322 Z" fill="url(#wingLeft)" role="img" aria-label="Chevron wing pattern along tube sides"/>
    <path d="M996 316 H1192 Q1160 560 1152 725 H1036 Q1028 560 996 316 Z" fill="url(#tubeBody)"/>
    <path d="M996 316 Q1028 560 1036 725" fill="none" stroke="var(--blue)" stroke-width="3"/>
    <path d="M1192 316 Q1160 560 1152 725" fill="none" stroke="var(--blue)" stroke-width="3"/>
    <path class="cap" d="M1034 725 H1152 V790 Q1152 804 1138 804 H1048 Q1034 804 1034 790 Z" fill="#1a1a1a"/>
    <path d="M1060 772 V752 Q1060 746 1066 746 H1120 Q1126 746 1126 752 V772" fill="none" stroke="#555" stroke-width="1.2"/>
  </svg>

  <!-- top lid panel -->
  <div class="abs brand" style="left:52px;top:140px;width:224px;font-size:30px"><span class="dot" style="width:14px;height:14px"></span>VANTRO #27</div>
  <div class="abs headline" style="left:52px;top:212px;width:224px;font-size:14.5px;color:var(--panel-black)">Men's<br>Natural Therapeutic<br>Intimate Wash</div>

  <!-- back (black) panel -->
  <div class="abs brand on-dark" style="left:52px;top:330px;width:224px;font-size:24px"><span class="dot" style="width:12px;height:12px"></span>VANTRO #27</div>
  <div class="abs headline" style="left:52px;top:380px;width:224px;font-size:14.5px;color:var(--white)">Men's<br>Natural Therapeutic<br>Intimate Wash</div>
  <div class="abs list" style="left:52px;top:467px;width:224px">
    Formula contains:<br>Tea Tree OIL<br>Aloe Vera Gel<br>Coconut Oil<br><br>Helps with<br>Jock Itch<br>(tinea cruris)<br>Skin Rashes<br>Candida<br>Itchy Skin
  </div>

  <!-- left side panel -->
  <div class="abs headline" style="left:276px;top:313px;width:128px;font-size:19.5px;line-height:20px;color:var(--white)">Men's<br>Natural<br>Therapeutic<br>Intimate<br>Wash</div>
  <div class="abs" style="left:276px;top:440px"><span class="helps-tab">Helps with</span></div>
  <ul class="abs bullets" style="left:294px;top:461px">
    <li>Jock Itch</li><li class="indent">(tinea cruris)</li><li>Skin Rashes</li><li>Candida</li><li>Itchy Skin</li>
  </ul>

  <!-- right side panel -->
  <div class="abs headline" style="left:740px;top:313px;width:126px;font-size:19.5px;line-height:20px;color:var(--white)">Men's<br>Natural<br>Therapeutic<br>Intimate<br>Wash</div>
  <div class="abs" style="left:753px;top:440px"><span class="helps-tab right">Helps with</span></div>
  <ul class="abs bullets" style="left:763px;top:461px">
    <li>Jock Itch</li><li class="indent">(tinea cruris)</li><li>Skin Rashes</li><li>Candida</li><li>Itchy Skin</li>
  </ul>

  <!-- front panel -->
  <div class="abs brand" style="left:440px;top:376px;width:264px;font-size:44px"><span class="dot" style="width:18px;height:18px"></span>VANTRO #27</div>
  <div class="abs label-band headline" style="left:490px;top:468px;width:162px;height:46px;font-size:12px;line-height:14px;padding-top:2px">
    <span style="color:var(--white)">Men's</span><br>Natural Therapeutic<br>Intimate Wash
  </div>
  <div class="abs small" style="left:500px;top:574px;width:144px;font-size:8.5px;line-height:10.5px">Formula contains:<br>Tea Tree OIL<br>Aloe Vera Gel<br>Coconut Oil</div>
  <div class="abs wash-box" style="left:512px;top:628px;width:118px;height:32px;font-size:16px;line-height:32px">WASH/SOAP</div>
  <div class="abs" style="left:500px;top:774px;width:144px;text-align:center;font-size:12px;color:#333">4 oz.</div>

  <!-- bottom flap (upside down) -->
  <div class="abs" style="left:458px;top:826px;width:226px;height:170px;transform:rotate(180deg)">
    <div class="brand" style="margin-top:20px;font-size:30px"><span class="dot" style="width:14px;height:14px"></span>VANTRO #27</div>
    <div class="headline" style="margin-top:16px;font-size:13px;line-height:16px;color:var(--panel-black)">Men's<br>Natural Therapeutic<br>Intimate Wash</div>
  </div>

  <!-- tube artwork -->
  <div class="abs brand" style="left:1010px;top:384px;width:168px;font-size:28px"><span class="dot" style="width:11px;height:11px"></span>VANTRO #27</div>
  <div class="abs label-band headline" style="left:1031px;top:458px;width:126px;height:38px;font-size:9px;line-height:11px;padding-top:3px">
    <span style="color:var(--white)">Men's</span><br>Natural Therapeutic<br>Intimate Wash
  </div>
  <div class="abs small" style="left:1040px;top:539px;width:108px;font-size:6.5px;line-height:8px">Formula contains<br>Tea Tree OIL<br>Aloe Vera Gel<br>Coconut Oil</div>
  <div class="abs wash-box" style="left:1047px;top:581px;width:94px;height:22px;font-size:12.5px;line-height:22px">WASH/SOAP</div>
  <div class="abs small" style="left:1030px;top:612px;width:128px;font-size:6.5px;line-height:10px">Helps with<br>Jock Itch (tinea cruris)<br>Skin Rashes<br>Candida<br>Itchy Skin</div>
  <div class="abs" style="left:1040px;top:693px;width:108px;text-align:center;font-size:9px;color:#333">4 oz.</div>

</div>
</body>
</html>
```